Onboarding project UI redesign

The web site is used to onboard clients via a video-identification process.
The end-user first tests his computer, then enters his order details and waits for an operator engagement.
When the operator engages the customer, they go through some identification steps together, ending on a contract signature page.

Target Market(s)

Finance B2C

Industry/Entity Type

Finance

Coding

Coded - Design and coding required

Number of Pages Required

5+ page

Font styles to use
Sans Serif

Requirements
Must have
• Professional UI
• Design for mobile devices

```html
<!DOCTYPE html>
<html lang="en">
<head>
<meta charset="utf-8">
<title>Novara Bank – Video Identification</title>
<link rel="stylesheet" href="https://fonts.googleapis.com/css2?family=Roboto:wght@400;500;700&display=swap">
<style>
  :root {
    --brand-blue: #0a4f95;
    --brand-title: #0b4f94;
    --page-bg: #efefef;
    --panel-light: #f6f6f6;
    --card-bg: #ffffff;
    --footer-bg: #343434;
    --timer-bg: #a7a7a7;
    --timer-dot: #6f6f6f;
    --text-dark: #222222;
    --text-light: #ffffff;
    --icon-grey: #6d6d6d;
    --accent-green: #6db33f;
    --ring-grey: #dedede;
    --chat-grey: #8c8c8c;
  }
  * { box-sizing: border-box; margin: 0; padding: 0; }
  html, body { width: 1200px; height: 675px; overflow: hidden; }
  body {
    font-family: "Roboto", Arial, sans-serif;
    background: var(--page-bg);
    color: var(--text-dark);
    position: relative;
  }
  .top-bar {
    position: absolute; left: 0; top: 0; width: 1200px; height: 44px;
    background: var(--brand-blue);
  }
  .brand-name {
    position: absolute; left: 44px; top: 0; height: 44px;
    display: flex; align-items: center;
    font-size: 16px; font-weight: 400; color: var(--text-light);
  }
  .date-time {
    position: absolute; right: 44px; top: 0; height: 44px;
    display: flex; align-items: center; gap: 16px;
    color: var(--text-light); font-size: 12.4px;
  }
  .session-card {
    position: absolute; left: 44px; top: 70px; width: 1112px; height: 512px;
    background: var(--card-bg);
    box-shadow: 0 2px 14px rgba(0,0,0,0.08);
    display: flex;
  }
  .video-panel {
    position: relative; width: 527px; height: 100%;
    background: var(--panel-light);
  }
  .rec-timer {
    position: absolute; left: 22px; top: 13px; width: 105px; height: 31px;
    background: var(--timer-bg); border-radius: 2px;
    display: flex; align-items: center; padding-left: 18px; gap: 6px;
    color: var(--text-light); font-weight: 700; font-size: 12.4px;
  }
  .rec-dot { width: 15px; height: 15px; border-radius: 50%; background: var(--timer-dot); }
  .connection {
    position: absolute; left: 114px; top: 244px; width: 300px; height: 32px;
  }
  .connection-label {
    position: absolute; left: 0; right: 0; top: -12px; text-align: center;
    font-size: 10px; line-height: 12px; color: var(--text-dark);
  }
  .step-panel { position: relative; flex: 1; }
  .step-progress { position: absolute; left: 22px; top: 18px; width: 54px; height: 54px; }
  .step-count {
    position: absolute; left: 22px; top: 18px; width: 54px; height: 54px;
    display: flex; align-items: center; justify-content: center;
    font-size: 10px; color: #888;
  }
  .step-count strong { font-size: 15px; color: var(--text-dark); font-weight: 700; margin-right: 1px; }
  .step-text { position: absolute; left: 97px; top: 30px; }
  .step-index { font-size: 10px; }
  .step-title { margin-top: 3px; font-size: 12.3px; font-weight: 700; color: var(--brand-title); letter-spacing: 0.1px; }
  .step-body { margin-top: 11px; font-size: 12.6px; }
  .bottom-bar {
    position: absolute; left: 0; top: 609px; width: 1200px; height: 66px;
    background: var(--footer-bg);
  }
  .chat-button {
    position: absolute; left: 1124px; top: 625px; width: 31px; height: 31px;
  }
</style>
</head>
<body>
  <header class="top-bar">
    <div class="brand-name">Novara Bank</div>
    <div class="date-time"><span>Friday, March 22, 2019</span><span>11:12 AM</span></div>
  </header>

  <main class="session-card">
    <section class="video-panel">
      <div class="rec-timer"><span class="rec-dot"></span><span>00:00:00</span></div>
      <div class="connection">
        <div class="connection-label">Connecting, please wait...</div>
        <svg width="300" height="32" viewBox="0 0 300 32" fill="none" stroke="var(--icon-grey)" stroke-width="1">
          <g class="terminal">
            <rect x="0.5" y="1.5" width="30" height="22" rx="1"/>
            <circle cx="15.5" cy="1.5" r="1.6" fill="#fff"/>
            <line x1="20" y1="6" x2="26" y2="6"/>
            <circle cx="15.5" cy="11" r="3"/>
            <path d="M9 20 q6.5 -7 13 0"/>
            <line x1="15.5" y1="24" x2="15.5" y2="29"/>
            <line x1="8" y1="30" x2="23" y2="30"/>
          </g>
          <line x1="39" y1="15.5" x2="260" y2="15.5" stroke="var(--accent-green)" stroke-width="1.6" stroke-dasharray="8 5"/>
          <g class="terminal" transform="translate(268 0)">
            <rect x="0.5" y="1.5" width="30" height="22" rx="1"/>
            <circle cx="15.5" cy="1.5" r="1.6" fill="#fff"/>
            <line x1="20" y1="6" x2="26" y2="6"/>
            <circle cx="15.5" cy="11" r="3"/>
            <path d="M9 20 q6.5 -7 13 0"/>
            <line x1="15.5" y1="24" x2="15.5" y2="29"/>
            <line x1="8" y1="30" x2="23" y2="30"/>
          </g>
        </svg>
      </div>
    </section>

    <section class="step-panel">
      <svg class="step-progress" viewBox="0 0 54 54">
        <circle cx="27" cy="27" r="24.5" fill="none" stroke="var(--ring-grey)" stroke-width="4"/>
        <circle cx="27" cy="27" r="24.5" fill="none" stroke="var(--accent-green)" stroke-width="4"
                stroke-dasharray="14 200" transform="rotate(-90 27 27)"/>
      </svg>
      <div class="step-count"><strong>1</strong>/11</div>
      <div class="step-text">
        <p class="step-index">Step 1.</p>
        <h1 class="step-title">WAITING FOR OPERATOR</h1>
        <p class="step-body">Welcome, a few more minutes and you can activate your new novarabank account.</p>
      </div>
    </section>
  </main>

  <footer class="bottom-bar"></footer>
  <svg class="chat-button" viewBox="0 0 31 31" aria-label="Chat">
    <circle cx="15.5" cy="15.5" r="15.5" fill="var(--chat-grey)"/>
    <path d="M12 9 h10 a3 3 0 0 1 3 3 v4 a3 3 0 0 1 -3 3 h-1 v3 l-3 -3 h-6 a3 3 0 0 1 -3 -3 v-4 a3 3 0 0 1 3 -3z" fill="#fff"/>
    <path d="M8 13 a3 3 0 0 0 -2 3 v3 a3 3 0 0 0 3 3 v2 l3 -2 h5" fill="none" stroke="#fff" stroke-width="1.3"/>
  </svg>
</body>
</html>
```